Sweet website for Velmora Flowers

Our name is Velmora and we are looking for someone to design a SWEET looking website for us. We would like a site that has a responsive design, clean interface, easy to navigate and smooth user experience. It will be hosted on wordpress and is an ecommerce site so it needs to be fully compatible so that updates can be made easily on the back end.

It is important to us that the design is premium looking, beautiful to look at and has an elegance to it that befits the beautiful products we sell. We don't want it to look like a standard wordpress template so please feel free to be creative.

We have defined basic template pages in wireframes which are NOT by any means a design mandate. Please use this as a guide for what content should be considered in the design on each page. THERE ARE TWO HOMEPAGE OPTIONS (1 has additional content areas - please propose designs for both options) We DO NOT want to see creative that looks exactly like our wireframes. Please come up with fresh creative ideas. (see wireframe doc attached). We have also attached the copy deck, logos, design references to help you to better understand what our customers like.

THANK YOU! LOOKING FORWARD TO SEEING YOUR PROPOSALS!!!
Updates

An updated content/wireframe document has been uploaded. We have 2 content options for the homepage - please propose designs for both layouts.

We have also added a powerpoint with websites that we like so that you can get a better idea of what we would like our website to look like.

Reason: We are extending the deadline and have increased and guaranteed the payment since we can see potential in the submitted designs but feel that they are currently not at their creative potential. The extra time given should allow for more time to submit original designs that do not look exactly like the wireframes provided.

Target Market(s)

Premium, affluent market

Font styles to use
Sans Serif

Requirements
Must have
• see wireframe, copy and design reference attachments and use as guidelines. The powerpoint presentation shows key areas that we think will be good in our design. Please review them. There are 2 homepage content options. Please propose options for both.
Please take note that option 2 has 3 additional content areas labelled "hand tied bouquets shop now", "Hatbox arrangements shop now" "floral cupcakes shop now" please propose 1 design with this the additional sections and 1 design without.

```html
<!DOCTYPE html>
<html lang="en">
<head>
<meta charset="utf-8">
<title>Velmora Flowers</title>
<link rel="stylesheet" href="https://fonts.googleapis.com/css2?family=Ubuntu:wght@300;400;500;700&family=Josefin+Sans:wght@400;600&display=swap">
<style>
:root{
  --pink:#e0487a;
  --pink-deep:#b8245a;
  --wine:#8c1a45;
  --grey-dark:#5b5b5b;
  --text:#3a3a3a;
  --green:#4e7a2d;
  --green-dark:#2f5a17;
  --white:#ffffff;
}
*{box-sizing:border-box;margin:0;padding:0}
html,body{width:940px;height:1200px;overflow:hidden}
body{
  position:relative;
  font-family:"Ubuntu",sans-serif;
  color:var(--text);
  background:
    radial-gradient(circle at 8% 30%,#f6cdd8 0,rgba(246,205,216,0) 180px),
    radial-gradient(circle at 95% 22%,#f8d6df 0,rgba(248,214,223,0) 200px),
    radial-gradient(circle at 50% 58%,#f6d3dc 0,rgba(246,211,220,0) 260px),
    radial-gradient(circle at 10% 85%,#f6d6de 0,rgba(246,214,222,0) 200px),
    linear-gradient(#fbeef2,#f9e6ec);
}
.abs{position:absolute}

/* top bar */
.topbar{left:0;top:0;width:940px;height:29px;background:linear-gradient(#8a8a8a,#5e5e5e)}
.account-links{left:290px;top:5px;display:flex;gap:4px}
.account-links a{display:block;font-size:9px;color:var(--white);text-decoration:none;padding:4px 8px;background:linear-gradient(#7d7d7d,#555);border-radius:3px}
.social-line{right:68px;top:8px;font-size:9px;color:var(--white);display:flex;align-items:center;gap:4px}
.social-box{width:12px;height:12px;background:#d9d9d9;border-radius:2px;display:inline-block}

/* brand */
.brand-box{left:79px;top:0;width:197px;height:123px;background:var(--white);box-shadow:0 4px 8px rgba(0,0,0,.12);display:flex;flex-direction:column;align-items:center;justify-content:center}
.brand-mark{width:26px;height:26px;border-radius:50%;background:var(--pink);margin-bottom:8px}
.brand-name{font-size:17px;font-weight:500;color:var(--pink-deep);letter-spacing:1px}
.tagline{left:289px;top:54px;font-family:"Josefin Sans",sans-serif;font-variant:small-caps;font-size:24px;line-height:21px;color:var(--pink);letter-spacing:.5px}

.newsletter{left:474px;top:35px;width:226px;height:82px;border-left:1px solid #e7a0b4;padding-left:14px}
.newsletter h4{font-size:8.5px;font-weight:700;color:#333}
.newsletter p{font-size:8.5px;line-height:10.5px;color:#333}
.signup{display:flex;gap:2px;margin-top:3px}
.signup span{display:block;width:124px;height:13px;background:var(--white);border:1px solid #ccc;font-size:6px;padding:2px 3px;color:#555}
.signup b{display:block;height:13px;padding:2px 7px;font-size:7px;font-weight:400;color:var(--white);background:linear-gradient(#8a8a8a,#5a5a5a);border-radius:3px}
.newsletter .secret{font-size:11px;color:var(--pink);margin-top:3px}
.contact{left:700px;top:35px;height:82px;border-left:1px solid #e7a0b4;padding-left:18px;font-size:10.5px;line-height:13.5px;color:var(--grey-dark)}
.contact strong{font-weight:700}
.dash-line{left:276px;top:122px;width:596px;border-top:1px dashed #e7a0b4}

/* nav */
.nav{left:67px;top:139px;width:805px;height:32px;background:linear-gradient(#d53a6e,#9a1c4c);border-radius:3px;display:flex;align-items:center;box-shadow:0 2px 4px rgba(0,0,0,.2)}
.nav a{font-size:9.5px;font-weight:500;color:var(--white);text-decoration:none;padding:0 9px;height:32px;line-height:32px;border-right:1px solid rgba(255,255,255,.25)}
.nav a.active{background:var(--wine);padding:0 11px}
.search{position:absolute;right:12px;top:9px;display:flex}
.search span{display:block;width:113px;height:15px;background:var(--white)}
.search b{display:block;height:15px;padding:0 7px;line-height:15px;font-size:8.5px;font-weight:400;color:var(--white);background:#7f1a42}

/* hero */
.hero{left:67px;top:178px;width:805px;height:342px;background:linear-gradient(90deg,#f4f1f2,#faf8f9);box-shadow:0 1px 4px rgba(0,0,0,.1);overflow:hidden}
.hero-photo{position:absolute;left:320px;top:10px;width:473px;height:332px;
  background:linear-gradient(160deg,#fbe9ee 0%,#f7b6c3 30%,#ef8ea1 55%,#f2a2b2 75%,#f6dde3 100%)}
.hero-title-light{position:absolute;left:37px;top:56px;font-size:28px;font-weight:300;color:var(--green)}
.hero-title-bold{position:absolute;left:37px;top:84px;font-size:32px;font-weight:700;color:var(--pink)}
.hero-copy{position:absolute;left:37px;top:126px;width:230px;font-size:10px;line-height:12px;color:#444}
.shop-now{position:absolute;left:37px;top:235px;padding:5px 9px;font-size:9px;font-weight:500;color:var(--white);background:linear-gradient(var(--green),var(--green-dark));border-radius:4px}
.dots{position:absolute;left:37px;top:306px;display:flex;gap:3px}
.dots i{width:8px;height:8px;border-radius:50%;background:#777}
.dots i.on{background:var(--pink-deep)}
.hero-arrows{position:absolute;left:715px;top:298px;display:flex;gap:5px}
.hero-arrows span{width:27px;height:26px;background:var(--wine);display:flex;align-items:center;justify-content:center}

/* feature cards */
.card{top:540px;width:253px;height:286px;background:#f4f4f4;border:1px solid #ddd}
.card-head{height:49px;background:linear-gradient(#e5507f,#a41e50);padding:0 9px;display:flex;align-items:center;font-size:12px;font-weight:700;color:var(--white);line-height:14px}
.card-photo{margin:8px 9px 0;height:123px;border:3px solid #bdbdbd}
.card p{margin:13px 9px 0;font-size:10px;line-height:12px;color:#444}

/* featured products */
.featured{left:67px;top:853px;width:805px;height:205px;background:var(--white);border:1px solid #e3e3e3}
.featured h2{position:absolute;left:10px;top:10px;font-size:17px;font-weight:700;color:var(--pink)}
.product{position:absolute;top:42px;width:200px;height:150px;text-align:center}
.product + .product{border-left:1px solid #ddd}
.product-photo{width:128px;height:132px;margin:-4px auto 0;border-radius:10px}
.price{position:absolute;left:38px;top:88px;width:42px;height:42px;border-radius:50%;background:radial-gradient(circle at 40% 35%,#e5507f,#a41e50);color:var(--white);font-size:11px;font-weight:700;line-height:11px;display:flex;flex-direction:column;align-items:center;justify-content:center;box-shadow:0 2px 3px rgba(0,0,0,.25)}
.product-name{position:absolute;left:0;width:200px;top:137px;font-size:10px;color:#333}
.feat-arrow{position:absolute;top:100px}

/* footer */
.footer{left:67px;top:1085px;width:805px;height:115px;background:linear-gradient(#9b9b9b,#6e6e6e);border-top:5px solid var(--pink)}
.footer h3{position:absolute;left:23px;top:17px;font-size:15px;font-weight:500;color:var(--white)}
.footer-contact{position:absolute;left:23px;top:42px;font-size:9.5px;line-height:18px;color:var(--white)}
.footer-contact div{display:flex;align-items:center;gap:4px}
.footer-social{position:absolute;left:23px;top:87px;display:flex;gap:4px}
.footer-social i{width:14px;height:14px;background:#cfcfcf;border-radius:2px}
.footer-divider{position:absolute;top:15px;width:1px;height:85px;background:rgba(255,255,255,.3)}
.copyright{position:absolute;left:208px;top:46px;font-size:9px;line-height:15px;color:var(--white)}
.footer-links{position:absolute;left:408px;top:53px;font-size:9px;color:var(--white);white-space:nowrap}
.footer-links span{margin:0 5px}
</style>
</head>
<body>

<div class="abs topbar"></div>
<nav class="abs account-links"><a>My Account</a><a>My Flower Basket</a></nav>
<div class="abs social-line">Like us on <i class="social-box"></i> Follow us on <i class="social-box"></i> and <i class="social-box"></i> for special offers!</div>

<div class="abs brand-box">
  <div class="brand-mark"></div>
  <div class="brand-name">Velmora Flowers</div>
</div>
<div class="abs tagline">When words<br>are not enough</div>

<div class="abs newsletter">
  <h4>CAN YOU KEEP A SECRET?</h4>
  <p>Join the Petal Society and get exclusive member only sales and delivery discounts when you sign up for the PETAL Newsletter!</p>
  <div class="signup"><span>Enter your email...</span><b>Sign up</b></div>
  <div class="secret">We won't tell if you don't tell!</div>
</div>
<div class="abs contact">Contact us on:<br><strong>+971555018247</strong><br>or Email us:<br><strong>info@velmoraflowers.com</strong></div>
<div class="abs dash-line"></div>

<nav class="abs nav">
  <a class="active">BUY FLOWERS</a><a>SEASON'S COLLECTION</a><a>WEDDINGS &amp; CONTRACTS</a><a>GIFTS &amp; ACCESSORIES</a><a>FREE UPDATES</a><a>BLOGS</a>
  <div class="search"><span></span><b>Search</b></div>
</nav>

<section class="abs hero">
  <div class="hero-photo" role="img" aria-label="Bunch of pink gerbera daisies"></div>
  <div class="hero-title-light">SOME TEXT HERE</div>
  <div class="hero-title-bold">SOME TEXT HERE</div>
  <p class="hero-copy">Some text here Some text here Some text here Some text here Some text here Some text here Some text here Some text here Some text here Some text here Some text here Some text here Some text here Some text here Some text here Some text here Some text here Some text here</p>
  <div class="shop-now">SHOP NOW</div>
  <div class="dots"><i class="on"></i><i></i><i></i><i></i><i></i><i></i></div>
  <div class="hero-arrows">
    <span><svg width="10" height="12" viewBox="0 0 10 12"><path d="M7 1 2 6l5 5" fill="none" stroke="#fff" stroke-width="2.4"/></svg></span>
    <span><svg width="10" height="12" viewBox="0 0 10 12"><path d="M3 1l5 5-5 5" fill="none" stroke="#fff" stroke-width="2.4"/></svg></span>
  </div>
</section>

<article class="abs card" style="left:67px">
  <div class="card-head">CUSTOMER FAVOURITES AND CLIENTS TESTIMONIALS</div>
  <div class="card-photo" role="img" aria-label="Group of smiling young customers" style="background:linear-gradient(90deg,#e8c9a9,#c99a78 40%,#9aa2b4 75%,#7d6e66)"></div>
  <p>Stuck on what to choose? Get inspired by our customer favourites. If you have something specific in mind or prefer a Bespoke arrangement or bouquet, contact us for a free consultation.</p>
</article>
<article class="abs card" style="left:342px">
  <div class="card-head">THE SWEET LIFE SOCIETY</div>
  <div class="card-photo" role="img" aria-label="Modern white villa with garden" style="background:linear-gradient(#8fb4d8,#dfe3e2 45%,#e9dccb 70%,#6f8f4a)"></div>
  <p>Come and join our community of taste makers where privileges include member specials and newsletter updates on what's hot and happening. Get ideas on selecting the best flowers for your loved one, your home or your wedding. Join today and get free delivery on your first order! It's just our little way of saying thank you!</p>
</article>
<article class="abs card" style="left:619px">
  <div class="card-head">OUR SERVICE GUARANTEE</div>
  <div class="card-photo" role="img" aria-label="Business handshake" style="background:linear-gradient(90deg,#2d2e33,#e9c3a6 45%,#d8b195 60%,#3a3b40)"></div>
  <p>At Velmora Flowers we are committed to excellence in the design and delivery of our floral services and products. If, for any reason, you are not 100% satisfied please contact us.</p>
</article>

<section class="abs featured">
  <h2>FEATURED PRODUCTS</h2>
  <svg class="feat-arrow" style="left:12px" width="12" height="16" viewBox="0 0 12 16"><path d="M9 2 3 8l6 6" fill="none" stroke="#b8245a" stroke-width="2.6"/></svg>
  <div class="product" style="left:0">
    <div class="product-photo" role="img" aria-label="Pink flowers in a hatbox" style="background:linear-gradient(#f4a9bf,#ee8fab 55%,#f6dbe4)"></div>
    <div class="price"><span>$</span><span>25.75</span></div>
    <div class="product-name">Flower name put here</div>
  </div>
  <div class="product" style="left:200px">
    <div class="product-photo" role="img" aria-label="Yellow lilies and roses in a vase" style="background:linear-gradient(#f3e27a,#ead25a 55%,#f1e6b6)"></div>
    <div class="price"><span>$</span><span>32.5</span></div>
    <div class="product-name">Flower name put here</div>
  </div>
  <div class="product" style="left:400px">
    <div class="product-photo" role="img" aria-label="Bright mixed gerbera bouquet" style="background:linear-gradient(#f27a4e,#ec5a3e 55%,#f4c9b8)"></div>
    <div class="price"><span>$</span><span>19.45</span></div>
    <div class="product-name">Flower name put here</div>
  </div>
  <div class="product" style="left:600px">
    <div class="product-photo" role="img" aria-label="Birthday flower bouquet in wrapping" style="background:linear-gradient(#f39a4a,#ee7fa0 55%,#f6c7d4)"></div>
    <div class="price"><span>$</span><span>41.40</span></div>
    <div class="product-name">Flower name put here</div>
  </div>
  <svg class="feat-arrow" style="left:782px" width="12" height="16" viewBox="0 0 12 16"><path d="M3 2l6 6-6 6" fill="none" stroke="#b8245a" stroke-width="2.6"/></svg>
</section>

<footer class="abs footer">
  <h3>GET IN TOUCH</h3>
  <div class="footer-contact">
    <div><svg width="9" height="9" viewBox="0 0 10 10"><path d="M2 0.5 4 3 3 4.3c.6 1.2 1.5 2.1 2.7 2.7L7 6l2.5 2L8.3 9.6C4 9.3.7 6 .4 1.7Z" fill="#fff"/></svg>+971555018247</div>
    <div><svg width="10" height="8" viewBox="0 0 10 8"><rect x=".5" y=".5" width="9" height="7" fill="#fff"/><path d="M.5 .5 5 4.5 9.5 .5" fill="none" stroke="#7a7a7a"/></svg>info@velmoraflowers.com</div>
  </div>
  <div class="footer-social"><i></i><i></i><i></i></div>
  <div class="footer-divider" style="left:187px"></div>
  <div class="copyright">Copyright 2013 www.velmora.com<br>All rights reserved.</div>
  <div class="footer-divider" style="left:387px"></div>
  <div class="footer-links">About Us<span>|</span>FAQs<span>|</span>Secure Payment<span>|</span>Policy<span>|</span>Terms and conditions<span>|</span>Contact us</div>
</footer>

</body>
</html>
```